Verin Court Nine Flash website

we need a website to cater to 2 aspect of the business. We have Verin court residence and verin court office. For the office, we will get their inquire and arrange a face to face meetup to show them the office area for rent. For the residence side, it will need to be like lodgly or staymira.com. we want to allow them to book online for the date they need. We have a total of 10 different room configurations starting at $70 per night and up depending on the size of the room. example of the design is https://pelvandale.com/

Target Market(s)

the website should have detail information on the layout, designs, and luxury of the building.

Industry/Entity Type

office and service appartment rental/lease

Coding

Coded - Design and coding required

Number of Pages Required

5+ page

Requirements
Must have
• a luxury perspective
Nice to have
• example https://pelvandale.com/

```html
<!DOCTYPE html>
<html lang="en">
<head>
<meta charset="utf-8">
<title>Verin Court Nine</title>
<link href="https://fonts.googleapis.com/css2?family=Cinzel:wght@400;500&family=Montserrat:wght@300;400;500;600&family=Lora:ital@1&display=swap" rel="stylesheet">
<style>
:root{
  --gold:#c9a04a;
  --gold-dark:#b88d33;
  --ink:#333;
  --muted:#777;
  --line:#e6dcc6;
  --footer:#4b4b4b;
  --white:#fff;
}
*{box-sizing:border-box;margin:0;padding:0}
html,body{width:1200px;height:4135px;overflow:hidden;background:var(--white)}
body{font-family:'Montserrat',sans-serif;color:var(--ink);position:relative}
.abs{position:absolute}
.section-title{position:absolute;left:0;width:1200px;text-align:center;font-weight:300;font-size:29px;color:#444}
.btn-outline{position:absolute;border:2px solid var(--gold);color:var(--gold);font-size:10px;font-weight:500;display:flex;align-items:center;justify-content:center;background:#fff;white-space:nowrap}
.btn-solid{position:absolute;background:var(--gold);color:#fff;font-size:10px;font-weight:500;display:flex;align-items:center;justify-content:center;white-space:nowrap}

/* hero */
.hero{position:absolute;left:0;top:0;width:1200px;height:561px;background:linear-gradient(160deg,#4a3c30 0%,#2e2620 45%,#5a3a2c 70%,#2a211c 100%)}
.hero-shade{position:absolute;inset:0;background:rgba(20,15,10,.35)}
.logo-box{position:absolute;left:0;top:0;width:150px;height:86px;background:#fff;display:flex;flex-direction:column;align-items:center;justify-content:center;gap:6px}
.logo-box .mark{width:26px;height:26px;border:1.5px solid var(--gold)}
.logo-box span{font-family:'Cinzel',serif;font-size:11px;color:#555;white-space:nowrap}
.nav{position:absolute;top:36px;left:522px;display:flex;gap:30px;font-size:10px;color:#fff;white-space:nowrap}
.nav .active{color:var(--gold)}
.nav-book{position:absolute;left:981px;top:24px;width:113px;height:36px;border:1px solid #ddd;color:#fff;font-size:10px;display:flex;align-items:center;justify-content:center}
.hero-welcome{position:absolute;top:181px;width:1200px;text-align:center;font-family:'Cinzel',serif;color:#fff;font-size:17px}
.hero-title{position:absolute;top:206px;width:1200px;text-align:center;font-family:'Cinzel',serif;color:#fff;font-size:46px;font-weight:500}
.hero-sub{position:absolute;top:273px;width:1200px;text-align:center;color:#fff;font-size:16px;font-weight:300}

/* amenities */
.amenity{position:absolute;width:206px;text-align:center;font-size:12px;color:#555}
.amenity svg{display:block;margin:0 auto 9px}

/* feature blocks */
.feature-title{position:absolute;font-size:17px;color:#333}
.feature-text{position:absolute;font-size:10.5px;line-height:18px;color:#777;width:270px}

/* rooms */
.room{position:absolute;top:2028px;width:314px;height:374px;background:#fff;box-shadow:0 1px 6px rgba(0,0,0,.08)}
.room-photo{height:214px;background:linear-gradient(180deg,#f1ede8 0%,#d9cfc2 55%,#8a6a45 100%)}
.room-tag{position:absolute;top:202px;left:115px;width:84px;height:24px;background:#7b7b7b;color:#fff;font-size:9px;display:flex;align-items:center;justify-content:center;clip-path:polygon(10% 0,90% 0,100% 100%,0 100%)}
.room-name{position:absolute;top:236px;width:100%;text-align:center;font-size:12px;font-weight:500}
.room-specs{position:absolute;top:280px;width:100%;display:flex;justify-content:space-around;font-size:8.5px;color:#777;text-align:center}
.room-specs svg{display:block;margin:0 auto 6px}

/* testimonial */
.quote-box{position:absolute;left:294px;top:2579px;width:613px;height:166px;border:1.5px solid var(--line);text-align:center}
.quote-mark{position:absolute;font-family:Georgia,serif;font-size:54px;color:var(--gold);line-height:1}

/* nearby */
.place{position:absolute;top:2961px;width:164px;text-align:center;font-size:12px;color:#555}
.place .circle{width:120px;height:120px;margin:0 auto 18px;border-radius:50%;border:4px solid #fff;box-shadow:0 0 0 1.5px var(--line)}
.place small{display:block;font-size:9px;color:#888;margin-top:4px}

/* faq */
.faq{position:absolute;left:255px;width:688px;font-size:11px;color:#333;display:flex;align-items:center}
.faq b{color:var(--gold);font-size:18px;font-weight:400;width:60px;padding-left:18px}
.faq-open{position:absolute;left:255px;top:3368px;width:688px;height:101px;background:var(--gold);color:#fff;padding:22px 30px 0 75px;font-size:11px}
.faq-open p{font-size:8.5px;line-height:13px;margin-top:18px}

/* footer */
.footer{position:absolute;left:0;top:3687px;width:1200px;height:448px;background:var(--footer);color:#fff}
.footer-brand{position:absolute;left:68px;top:74px;width:300px;text-align:center}
.footer-brand .mark{width:70px;height:86px;border:1.5px solid var(--gold);margin:0 auto}
.footer-brand .name{margin-top:22px;font-family:'Cinzel',serif;font-size:22px;color:var(--gold);white-space:nowrap}
.socials{position:absolute;left:166px;top:238px;display:flex;gap:10px}
.socials span{width:28px;height:28px;border-radius:50%;background:#3c3c3c}
.socials .on{background:var(--gold)}
.field{position:absolute;background:#fff;color:#555;font-size:9px;padding:7px 10px}
</style>
</head>
<body>

<!-- Hero -->
<section class="hero">
  <div role="img" aria-label="Hotel bedroom interior with bed, bench and patterned rug" class="abs" style="inset:0"></div>
  <div class="hero-shade"></div>
  <div class="logo-box"><div class="mark"></div><span>Verin Court Nine</span></div>
  <nav class="nav"><span class="active">Home</span><span>Design</span><span>Locations</span><span>Experience</span><span>About us</span><span>Contact us</span></nav>
  <div class="nav-book">Book Now!</div>
  <div class="hero-welcome">Welcome to</div>
  <div class="hero-title">Verin Court Nine</div>
  <div class="hero-sub">A charming 3-star hotel located in the heart of Harbour City.</div>
  <div class="btn-solid" style="left:544px;top:308px;width:113px;height:35px">Book Now!</div>
  <svg class="abs" style="left:593px;top:500px" width="14" height="20" viewBox="0 0 14 20"><path d="M7 1v17M2 13l5 5 5-5" stroke="#fff" stroke-width="1.5" fill="none"/></svg>
</section>

<!-- Amenities -->
<div class="section-title" style="top:628px">Exquisite Amenities</div>
<div class="amenity" style="left:187px;top:722px"><svg width="34" height="34"><rect x="4" y="14" width="26" height="16" fill="none" stroke="#333" stroke-width="2"/><rect x="10" y="5" width="12" height="9" fill="var(--gold)"/></svg>Front desk [24-hour]</div>
<div class="amenity" style="left:393px;top:722px"><svg width="34" height="34"><path d="M17 3v28M4 17l13-3 13 3M11 29l6-2 6 2" stroke="#333" stroke-width="2" fill="none"/><circle cx="17" cy="15" r="3" fill="var(--gold)"/></svg>Airport transfer</div>
<div class="amenity" style="left:600px;top:722px"><svg width="34" height="34"><circle cx="12" cy="10" r="7" fill="var(--gold)"/><rect x="8" y="18" width="20" height="10" rx="2" fill="none" stroke="#333" stroke-width="2"/></svg>Car parking</div>
<div class="amenity" style="left:805px;top:722px"><svg width="34" height="34"><path d="M6 8a20 20 0 0 1 20 20M6 15a13 13 0 0 1 13 13M6 22a6 6 0 0 1 6 6" stroke="#333" stroke-width="2" fill="none"/><circle cx="7" cy="27" r="3" fill="var(--gold)"/></svg>Free Wi-Fi in all rooms!</div>
<div class="amenity" style="left:187px;top:823px"><svg width="34" height="34"><rect x="3" y="7" width="28" height="12" fill="none" stroke="#333" stroke-width="2"/><path d="M8 23l-2 7M14 23l-1 7M20 23l1 7M26 23l2 7" stroke="var(--gold)" stroke-width="2"/></svg>Air conditioning</div>
<div class="amenity" style="left:393px;top:823px"><svg width="34" height="34"><rect x="6" y="11" width="14" height="19" fill="none" stroke="#333" stroke-width="2"/><rect x="20" y="15" width="9" height="15" fill="var(--gold)"/><path d="M10 11V5h6v6" stroke="#333" stroke-width="2" fill="none"/></svg>Luggage storage</div>
<div class="amenity" style="left:600px;top:823px"><svg width="34" height="34"><rect x="7" y="3" width="20" height="28" fill="none" stroke="#333" stroke-width="2"/><circle cx="17" cy="19" r="6" fill="var(--gold)"/></svg>Laundry service</div>
<div class="amenity" style="left:805px;top:823px"><svg width="34" height="34"><path d="M4 12h26M6 12v19h22V12M8 4h18l4 8H4z" stroke="#333" stroke-width="2" fill="none"/><rect x="13" y="19" width="8" height="12" fill="var(--gold)"/></svg>Coffee shop</div>
<div class="btn-outline" style="left:528px;top:914px;width:143px;height:37px">Contact Us Today!</div>

<!-- Residence -->
<div class="feature-title" style="left:105px;top:1113px">Verin Court Residence</div>
<div class="feature-text" style="left:105px;top:1149px">Lorem Ipsum is simply dummy text of the printing and typesetting industry. Lorem Ipsum has been the industry's standard dummy.</div>
<div class="btn-outline" style="left:105px;top:1221px;width:139px;height:37px">Book on Staymira</div>
<div class="abs" style="left:105px;top:1280px;width:139px;text-align:center;font-size:13px;color:#555">staymira</div>
<div role="img" aria-label="Residence bedroom with pendant lamps and large window" class="abs" style="left:407px;top:1013px;width:793px;height:403px;background:linear-gradient(120deg,#8a6d4a 0%,#c9ae86 40%,#e8dcc8 65%,#7a6450 100%)"></div>

<!-- Office -->
<div role="img" aria-label="Office lounge with yellow armchairs, chandelier and tall windows" class="abs" style="left:0;top:1494px;width:793px;height:403px;background:linear-gradient(110deg,#9a9188 0%,#dcd6cc 35%,#c9a45a 60%,#b8b4ae 100%)"></div>
<div class="feature-title" style="left:817px;top:1616px">Verin Court Office</div>
<div class="feature-text" style="left:817px;top:1652px">Lorem Ipsum is simply dummy text of the printing and typesetting industry. Lorem Ipsum has been the industry's standard dummy.</div>
<div class="btn-outline" style="left:817px;top:1724px;width:117px;height:37px">Inquire Now!</div>

<!-- Rooms -->
<div class="section-title" style="top:1966px">Rooms at Verin Court Hotel</div>
<div class="room" style="left:105px">
  <div role="img" aria-label="Superior twin room with two beds" class="room-photo"></div>
  <div class="room-tag">Type - A</div>
  <div class="room-name">Superior Twin Room</div>
  <div class="room-specs"><div><svg width="22" height="16"><rect x="2" y="5" width="18" height="9" fill="none" stroke="#777" stroke-width="1.5"/></svg>2 single beds</div><div><svg width="22" height="16"><rect x="4" y="2" width="13" height="13" fill="none" stroke="#777" stroke-width="1.5" stroke-dasharray="2 2"/></svg>25 m²/269 ft.</div><div><svg width="22" height="16"><rect x="4" y="1" width="14" height="14" fill="none" stroke="#777" stroke-width="1.5"/></svg>City view</div></div>
  <div class="btn-outline" style="left:95px;top:322px;width:124px;height:37px">Check Availability</div>
</div>
<div class="room" style="left:444px">
  <div role="img" aria-label="Superior double room with curtains" class="room-photo"></div>
  <div class="room-tag">Type - B</div>
  <div class="room-name">Superior Double Room</div>
  <div class="room-specs"><div><svg width="22" height="16"><rect x="2" y="5" width="18" height="9" fill="none" stroke="#777" stroke-width="1.5"/></svg>1 double bed</div><div><svg width="22" height="16"><rect x="4" y="2" width="13" height="13" fill="none" stroke="#777" stroke-width="1.5" stroke-dasharray="2 2"/></svg>20 m²/215 ft.</div><div><svg width="22" height="16"><rect x="4" y="1" width="14" height="14" fill="none" stroke="#777" stroke-width="1.5"/></svg>City view</div></div>
  <div class="btn-solid" style="left:95px;top:322px;width:124px;height:37px">Check Availability</div>
</div>
<div class="room" style="left:782px">
  <div role="img" aria-label="Standard single room with curtains" class="room-photo"></div>
  <div class="room-tag">Type - C</div>
  <div class="room-name">Standard Single Room</div>
  <div class="room-specs"><div><svg width="22" height="16"><rect x="2" y="5" width="18" height="9" fill="none" stroke="#777" stroke-width="1.5"/></svg>1 single bed</div><div><svg width="22" height="16"><rect x="4" y="2" width="13" height="13" fill="none" stroke="#777" stroke-width="1.5" stroke-dasharray="2 2"/></svg>18 m²/194 ft.</div><div><svg width="22" height="16"><rect x="4" y="1" width="14" height="14" fill="none" stroke="#777" stroke-width="1.5"/></svg>City view</div></div>
  <div class="btn-outline" style="left:95px;top:322px;width:124px;height:37px">Check Availability</div>
</div>

<!-- Testimonials -->
<div class="section-title" style="top:2509px">Testimonials From Our Guests</div>
<div class="quote-box">
  <div style="margin-top:26px;font-family:'Lora',serif;font-style:italic;font-size:17px;color:#333">“ It was closed already.”</div>
  <div style="margin-top:12px;font-family:'Lora',serif;font-style:italic;font-size:10px;line-height:19px;color:#555">It was closed when we arrived at midnight. They said that new owners took over the hotel.<br>Staymira.com should know this situation. You shouldn't let us book on web.</div>
  <div style="margin-top:6px;color:var(--gold);font-size:15px;letter-spacing:2px">★★★★★</div>
  <div style="margin-top:12px;font-size:11px;font-weight:500">Ayane <span style="font-weight:400;color:#888;font-size:9px">from Harbour City</span></div>
</div>
<div class="quote-mark" style="left:282px;top:2560px">“</div>
<div class="quote-mark" style="left:900px;top:2730px">”</div>
<div class="abs" style="left:200px;top:2650px;color:#999;font-size:16px">‹</div>
<div class="abs" style="left:994px;top:2650px;color:#999;font-size:16px">›</div>
<div class="btn-outline" style="left:545px;top:2783px;width:111px;height:35px">View All</div>

<!-- Nearby -->
<div class="section-title" style="top:2887px">Near by Locations</div>
<div class="place" style="left:187px"><div role="img" aria-label="Airplane in the sky" class="circle" style="background:linear-gradient(180deg,#6fa6d6,#d8e8f4)"></div>Airports<small>7.8 km</small></div>
<div class="place" style="left:352px"><div role="img" aria-label="Transit road at sunset" class="circle" style="background:linear-gradient(180deg,#e0a56a,#6a6f78)"></div>Public transportation<small>2.7 km</small></div>
<div class="place" style="left:516px"><div role="img" aria-label="Doctor with stethoscope" class="circle" style="background:linear-gradient(180deg,#eef0f2,#c9ced4)"></div>Hospital or clinic<small>230 m</small></div>
<div class="place" style="left:683px"><div role="img" aria-label="Shopping mall interior" class="circle" style="background:linear-gradient(180deg,#b9bcc0,#8c7a62)"></div>Shopping<small>1.0 km</small></div>
<div class="place" style="left:847px"><div role="img" aria-label="Cash machine" class="circle" style="background:linear-gradient(180deg,#3e444a,#8a8f94)"></div>Cash withdrawal<small>190 m</small></div>
<div class="btn-outline" style="left:530px;top:3159px;width:139px;height:35px">View All Nearby</div>

<!-- FAQ -->
<div class="section-title" style="top:3261px">Frequently Asked Question</div>
<div class="faq" style="top:3336px;height:24px"><b>+</b>Does Verin Court Hotel provide airport transfer?</div>
<div class="faq-open">Does Verin Court Hotel provide laundry services?
  <p>Yes! Verin Court Hotel offers laundry service at your convenience for whenever you need your favorite shirts or dresses clean and fresh all throughout your vacation. Please contact the property for more information.</p>
  <span class="abs" style="left:20px;top:18px;font-size:18px">−</span>
</div>
<div class="faq" style="top:3475px;height:24px"><b>+</b>What are the property's policies for children's bedding at Verin Court Hotel?</div>
<div class="faq" style="top:3525px;height:24px"><b>+</b>How many floors does Verin Court Hotel have?</div>
<div class="faq" style="top:3576px;height:24px"><b>+</b>What payment cards are supported at Verin Court Hotel?</div>

<!-- Footer -->
<footer class="footer">
  <div class="footer-brand">
    <div class="mark"></div>
    <div class="name">Verin Court Nine</div>
  </div>
  <div class="socials"><span></span><span class="on"></span><span></span></div>
  <div class="abs" style="left:407px;top:75px;font-size:12px;font-weight:500">Contact Us</div>
  <svg class="abs" style="left:409px;top:102px" width="12" height="12"><path d="M2 2l3 0 1 3-2 1a8 8 0 0 0 3 3l1-2 3 1v3A10 10 0 0 1 2 2z" fill="var(--gold)"/></svg>
  <div class="abs" style="left:430px;top:98px;font-size:15px">(555) 0192-448</div>
  <svg class="abs" style="left:409px;top:141px" width="12" height="10"><rect x="0" y="1" width="12" height="8" fill="var(--gold)"/></svg>
  <div class="abs" style="left:430px;top:139px;font-size:10px">info@verincourtnine.com</div>
  <svg class="abs" style="left:409px;top:178px" width="10" height="14"><path d="M5 14S0 8 0 5a5 5 0 0 1 10 0c0 3-5 9-5 9z" fill="var(--gold)"/></svg>
  <div class="abs" style="left:430px;top:177px;font-size:11px;color:var(--gold)">Verin Court Nine</div>
  <div class="abs" style="left:430px;top:195px;font-size:9.5px;line-height:17px;width:190px">#42, Lane 18, Riverside Quarter, Old Market District, Harbour City, 40210</div>
  <div class="field" style="left:694px;top:76px;width:195px;height:30px">Name</div>
  <div class="field" style="left:900px;top:76px;width:195px;height:30px">Phone</div>
  <div class="field" style="left:694px;top:119px;width:401px;height:30px">Email Address</div>
  <div class="field" style="left:694px;top:162px;width:401px;height:66px">Message</div>
  <div class="abs" style="left:694px;top:240px;width:94px;height:37px;border:1.5px solid var(--gold);color:var(--gold);font-size:10px;display:flex;align-items:center;justify-content:center">Send</div>
  <div class="abs" style="left:0;top:360px;width:1200px;text-align:center;font-size:9px;color:#ddd">© 2024 <span style="color:var(--gold)">Verin Court Nine</span>. All Rights Reserved. &nbsp;&nbsp;&nbsp;&nbsp;|&nbsp;&nbsp;&nbsp;&nbsp; Privacy policy &nbsp;&nbsp;&nbsp;&nbsp;|&nbsp;&nbsp;&nbsp;&nbsp; Cookie policy &nbsp;&nbsp;&nbsp;&nbsp;|&nbsp;&nbsp;&nbsp;&nbsp; Terms of use</div>
  <svg class="abs" style="left:1137px;top:356px" width="18" height="20"><path d="M9 1l8 18-8-5-8 5z" fill="var(--gold)"/></svg>
</footer>

</body>
</html>
```